Squarespace website build: Quirk literary annual (initial design work supplied)

Our brand guidelines provide the look and feel for the website - we just need someone to create it based on our mock ups!
PLEASE NOTE:
- Please base our website off the website pages within the brief (ie homepage is GREEN)
- please ensure each page will be standalone (not a scrolling home page)
- please only use filtered duotone style photography as a hold, if you think the page needs a photo.
-please not the websites i have provided as an influence - especially TIDE YEARLY. We want very little photography.

Quirk is a literary and arts journal that provides a platform for both emerging and established writers and artists from New Zealand and beyond. We are passionate about sharing insights into the intimate and unique worlds of creatives with short stories, poetry, and art – showcasing raw and unfiltered glimpses into their world.

We have our brand guidelines and logo finalised, with a 'look and feel' design for the website within our attached brand guidelines document. We just need someone to design this simple website on Squarespace for us. It will have five pages and will need a newsletter sign up link:
Home page
About us page
Submissions page
Purchase page
Contact page

DRAFT WEB COPY

ABOUT
QUIRK is an independent literary annual journal established in 2022 by Hazel Wintergate and Mereana Clift that publishes unrepentant unfiltered accounts of life, eclectic takes on the mundane ordinary, and deep dives into modern love & sexuality.
Founder, Editor: Hazel Arohanui Wintergate
Founder, Production Director: Mereana Clift
Art Direction: Lorna Pike
Editorial Assistant: Kirsten Holloway-Dunn

I suggest duotone fashion-esque photography which is very Vesna Kordell/ Palm Springs vibe but not obviously identifiable.
· I love the style of Rufus Tennick for our shoot in particular. Group lazing around a pool, leisurely, glam, but effortless and ironically looking very natural – as though – yes, these are our lives.
SUBMISSION PAGE
Quirk welcomes submissions all year round.
We are drawn to dark humour, satirical takes on the social scene, and starkly honest accounts of ordinary life. Diversity is celebrated, adversity is welcomed and, above all, personal expression is championed. We are particularly seeking content that takes risks, screams of honesty and celebrates life’s most extraordinary moments.
Selected works will be published in our annual publication.

Submission guidelines
We accept flash fiction, short stories and poetry. Individual entries not to mustn’t exceed 2000 words.
Submitted work must be unpublished and in English. We welcome simultaneous submissions, but must be notified immediately if your manuscript is accepted for publication elsewhere or appears in any print or online source. We will endeavour to respond to all submissions within four weeks.
Please send submissions as a word document along with a brief bio of 50 words to pages@quirkjournal.test
PO Box[EB2]
​Note on Copyright: Copyright remains with the author.

Annual short story competition
Volume Alpha is interested in all that is spiritual, coincidental, or mysterious. Stories selected for this issue reflect life’s uncanny moments, those that defy explanation, and experiences that promote personal and spiritual growth. Entires must be no longer than 2000 words.

First prize: 1000
Second prize: 500
Third prize: 200[EB3]

SUPPORT US
Since our launch in 2022, we have relied upon the generous support of our creative business community in Wellington City, New Zealand. If you read us, or love our ethos, please consider a donation.
Link to chipinhere page
Updates

Hello designers
I would ideally love to have someone turn this around within a few weeks, because the design work has mostly been provided.
Thanks
Hazel

Hi everyone Please ensure you read our brand guidelines and follow the brief. Please note we do not yet have a product, as this is a new venture, so there is no point including images of a magazine that doesn't yet exist. Some further comment to ensure we get there: - We want all pages to be separate pages (not a scrolling home page) with a different colour based on the guidelines - The home page must look just as it does in the brand guidelines - There is no archive page (please read brief) as we have no archive yet. The pages are: Home, About, Contact, Competitions and submissions Thank you

Target Market(s)

writers and creatives

Industry/Entity Type

Writing/ creative/ publishing

Coding

Coded - Design and coding required

Number of Pages Required

4 page

Font styles to use
Other font styles liked:
• COTTA and Univers - as per brand guidelines

Requirements
Must have
• Squarespace designer needed to design our mocked up webpages.
Nice to have
• As close to the brand guideline mock ups as possible (see page 11,12,13)
Should not have
• anything outside of the brand guidelines

```html
<!DOCTYPE html>
<html lang="en">
<head>
<meta charset="utf-8">
<title>Quirk — Home and About pages</title>
<link href="https://fonts.googleapis.com/css2?family=Italiana&family=Oswald:wght@400;500&family=Inter:wght@400&display=swap" rel="stylesheet">
<style>
:root{
  --rose:#bd5874;
  --olive:#657834;
  --mustard:#b99b2b;
  --mustard-deep:#b69c2a;
  --cream:#f5f5f4;
  --white:#ffffff;
  --ink:#4a4a4a;
  --crimson:#b3304f;
  --crimson-dark:#8e1f3a;
  --berry:#a53e62;
  --display:"Italiana", "Times New Roman", serif;
  --label:"Oswald", "Arial Narrow", sans-serif;
  --body:"Inter", Arial, sans-serif;
}
*{margin:0;padding:0;box-sizing:border-box}
html,body{width:731px;height:1200px;overflow:hidden}
body{position:relative;background:var(--rose);font-family:var(--body);color:var(--white)}
.section-title{position:absolute;left:0;width:731px;text-align:center;font-family:var(--display);font-size:24px;font-weight:400;color:var(--white);line-height:1}
.page{position:absolute;left:83px;width:565px;overflow:hidden;box-shadow:0 12px 28px rgba(90,20,40,.25)}
.page--home{top:92px;height:471px;background:var(--olive)}
.page--about{top:648px;height:471px;background:var(--mustard-deep)}
.page > *{position:absolute}
.nav-link{font-family:var(--label);font-size:8px;font-weight:400;color:var(--white);line-height:1;white-space:nowrap}
.nav-link.is-active::after{content:"";position:absolute;left:1px;right:1px;bottom:-5px;height:1px;background:var(--white)}
.wordmark{font-family:var(--display);font-size:44px;line-height:1;left:0;width:565px;text-align:center;pointer-events:none}
.page--home .wordmark{color:var(--mustard)}
.page--about .wordmark{color:var(--olive)}
.call-button{height:20px;width:117px;display:flex;align-items:center;justify-content:center;gap:4px;font-family:var(--label);font-weight:500;font-size:8px;letter-spacing:.6px;color:var(--white);white-space:nowrap}
.page--home .call-button{background:var(--mustard)}
.page--about .call-button{background:var(--olive)}
.call-button .divider{width:1px;height:10px;background:var(--white)}
.title-rule{height:1px;background:rgba(255,255,255,.8)}
.headline{left:0;width:565px;text-align:center;font-family:var(--display);font-size:25px;line-height:29px;font-weight:400}
.read-button{left:236px;top:210px;width:93px;height:27px;border:1px solid rgba(255,255,255,.35);padding:2px}
.read-button span{display:flex;height:100%;align-items:center;justify-content:center;gap:6px;background:var(--mustard);font-family:var(--label);font-weight:500;font-size:7.5px;letter-spacing:.8px}
.photo-frame{border:1px solid;border-bottom:none}
.page--home .photo-frame{border-color:var(--mustard)}
.page--about .photo-frame{border-color:var(--olive)}
.hero-photo{left:70px;top:276px;width:425px;height:170px;background:linear-gradient(115deg,var(--crimson) 0%,#c04263 45%,var(--crimson-dark) 55%,var(--crimson) 70%,#bb3c5c 100%);clip-path:polygon(0 8px,12px 8px,18px 0,407px 0,413px 8px,425px 8px,425px 100%,0 100%)}
.site-footer{left:0;bottom:0;width:565px;height:25px;background:var(--cream);color:var(--ink);font-family:var(--body);font-size:7px;letter-spacing:.5px;display:flex;align-items:center;justify-content:center}
.intro{left:118px;top:157px;width:330px;text-align:center;font-family:var(--body);font-size:7.4px;line-height:13px;color:var(--white)}
.portrait{left:63px;top:247px;width:155px;height:170px;background:linear-gradient(160deg,#b8476c 0%,var(--berry) 55%,#8f3354 100%);clip-path:polygon(0 8px,12px 8px,18px 0,137px 0,143px 8px,155px 8px,155px 100%,0 100%)}
.team{left:274px;top:273px;width:180px;border-top:1px solid rgba(255,255,255,.4);border-bottom:1px solid rgba(255,255,255,.4);padding:9px 0;list-style:none}
.team li{white-space:nowrap;line-height:19px}
.team .role{font-family:var(--display);font-size:11px}
.team .name{font-family:var(--body);font-size:7.4px}
</style>
</head>
<body>

<h2 class="section-title" style="top:45px">Home Page</h2>

<section class="page page--home" aria-label="Home page">
  <a class="nav-link is-active" style="left:44px;top:31px">HOME</a>
  <a class="nav-link" style="left:79px;top:31px">ABOUT</a>
  <a class="nav-link" style="left:116px;top:31px">COMPETITIONS &amp; SUBMISSIONS</a>
  <div class="wordmark" style="top:10px">quirk</div>
  <a class="nav-link" style="left:357px;top:31px">CONTACT</a>
  <a class="call-button" style="left:405px;top:25px">
    <svg width="10" height="10" viewBox="0 0 24 24" fill="none" stroke="#fff" stroke-width="1.8"><path d="M5 3h4l2 5-3 2a12 12 0 0 0 6 6l2-3 5 2v4a2 2 0 0 1-2 2A17 17 0 0 1 3 5a2 2 0 0 1 2-2z"/></svg>
    <span class="divider"></span>CALL US: 555010-4477
  </a>

  <div class="title-rule" style="left:164px;top:102px;width:237px"></div>
  <h1 class="headline" style="top:107px">Quirk is a plucky little<br>pubication out of&nbsp; Wellington<br>New Zealand</h1>
  <a class="read-button"><span>READ HERE
    <svg width="10" height="5" viewBox="0 0 10 5" fill="none" stroke="#fff" stroke-width=".8"><path d="M0 2.5H9M7 .5L9 2.5 7 4.5"/></svg></span></a>

  <div class="photo-frame" style="left:59px;top:264px;width:447px;height:190px"></div>
  <div class="hero-photo" role="img" aria-label="Duotone crimson photograph of a building facade with angled balconies"></div>

  <footer class="site-footer">Copyright © 2022 Quirk Annual. All rights reserved.</footer>
</section>

<h2 class="section-title" style="top:600px">About Page</h2>

<section class="page page--about" aria-label="About page">
  <a class="nav-link" style="left:44px;top:31px">HOME</a>
  <a class="nav-link is-active" style="left:79px;top:31px">ABOUT</a>
  <a class="nav-link" style="left:116px;top:31px">COMPETITIONS &amp; SUBMISSIONS</a>
  <div class="wordmark" style="top:10px">quirk</div>
  <a class="nav-link" style="left:357px;top:31px">CONTACT</a>
  <a class="call-button" style="left:405px;top:25px">
    <svg width="10" height="10" viewBox="0 0 24 24" fill="none" stroke="#fff" stroke-width="1.8"><path d="M5 3h4l2 5-3 2a12 12 0 0 0 6 6l2-3 5 2v4a2 2 0 0 1-2 2A17 17 0 0 1 3 5a2 2 0 0 1 2-2z"/></svg>
    <span class="divider"></span>CALL US: 555010-4477
  </a>

  <div class="title-rule" style="left:213px;top:102px;width:140px"></div>
  <h1 class="headline" style="top:108px">About Quirk</h1>
  <p class="intro">QUIRK is an independent literary annual journal established in 2022 by Hazel Wintergate and Mereana Clift that publishes unrepentant unfiltered accounts of life, eclectic takes on the mundane ordinary, and deep dives into modern love &amp; sexuality.</p>

  <div class="photo-frame" style="left:52px;top:235px;width:177px;height:190px"></div>
  <div class="portrait" role="img" aria-label="Duotone pink portrait photograph of the editor"></div>

  <ul class="team">
    <li><span class="role">Founder&nbsp; Editor : </span><span class="name">Hazel Arohanui Wintergate</span></li>
    <li><span class="role">Founder&nbsp; Production Director : </span><span class="name">Mereana Clift</span></li>
    <li><span class="role">Art Direction : </span><span class="name">Lorna Pike</span></li>
    <li><span class="role">Editorial Assistant : </span><span class="name">Kirsten Holloway-Dunn</span></li>
  </ul>

  <footer class="site-footer">Copyright © 2022 Quirk Annual. All rights reserved.</footer>
</section>
</body>
</html>
```